Dietitian clinic needs a business card design

We need a business card design for a new dietitian group based in Singapore called "Brightpath and Bloom". We provide expert, personalised nutrition care to support a wide range of health needs, from chronic conditions to mindful eating. Our team also offers consulting, speaking, and tailored solutions for healthcare providers, organisations, and food services.

Target Market(s)

Adults

Industry/Entity Type

Healthcare

Contact Information for Business Card

Name, position, contact number, email, website address, our logo

Requirements
Nice to have
• Clean, professional but welcoming look

```html
<!DOCTYPE html>
<html lang="en">
<head>
<meta charset="utf-8">
<title>Brightpath and Bloom – Business Card</title>
<link href="https://fonts.googleapis.com/css2?family=Playfair+Display:wght@700&family=Tinos:wght@400;700&display=swap" rel="stylesheet">
<style>
  :root {
    --backdrop: #1e1f23;
    --teal: #245a6b;
    --teal-deep: #1f4f5f;
    --teal-soft: #2c6678;
    --paper: #ffffff;
    --ink: #1b1b1b;
    --rule: #3a3a3a;
  }
  * { margin: 0; padding: 0; box-sizing: border-box; }
  html, body {
    width: 1200px; height: 900px; overflow: hidden;
    background: var(--backdrop);
  }
  .stage {
    width: 1200px; height: 900px;
    display: flex; flex-direction: column;
    align-items: center; justify-content: center; gap: 40px;
  }
  .card {
    width: 700px; height: 400px;
    border-radius: 26px;
    position: relative; overflow: hidden;
  }
  /* Back */
  .card-back { background: var(--teal); }
  .card-back .pattern-field {
    position: absolute; inset: 0;
    background: linear-gradient(135deg, var(--teal-soft), var(--teal-deep));
  }
  .brand-name {
    font-family: "Tinos", "Times New Roman", serif;
    font-weight: 700; white-space: nowrap;
  }
  .card-back .brand-name {
    position: absolute; right: 80px; top: 160px;
    color: var(--paper); font-size: 24px;
  }
  /* Front */
  .card-front { background: var(--paper); display: flex; }
  .front-brand {
    width: 360px; display: flex; align-items: center; justify-content: center;
    color: var(--teal);
  }
  .front-brand .brand-name { font-size: 32px; }
  .divider {
    width: 1px; background: var(--rule);
    margin: 70px 0;
  }
  .contact {
    flex: 1; padding: 70px 30px 0 36px;
    font-family: "Tinos", "Times New Roman", serif;
    color: var(--ink);
  }
  .person-name {
    font-family: "Playfair Display", Georgia, serif;
    font-weight: 700; font-size: 27px; color: var(--teal);
    letter-spacing: 0.5px; text-transform: uppercase;
  }
  .person-role { font-size: 18px; margin-top: 6px; }
  .address { font-size: 17px; line-height: 1.3; margin-top: 22px; }
  .contact-list { list-style: none; margin-top: 24px; }
  .contact-list li {
    display: flex; align-items: center; gap: 12px;
    font-size: 17px; line-height: 1.55;
  }
  .contact-list svg { width: 16px; height: 16px; flex: none; fill: var(--teal); }
</style>
</head>
<body>
<main class="stage">
  <section class="card card-back">
    <div class="pattern-field" role="img" aria-label="Embossed repeating tonal teal pattern"></div>
    <span class="brand-name">Brightpath and Bloom</span>
  </section>

  <section class="card card-front">
    <div class="front-brand">
      <span class="brand-name">Brightpath and Bloom</span>
    </div>
    <div class="divider"></div>
    <div class="contact">
      <h1 class="person-name">Daniel Reyes</h1>
      <p class="person-role">Managing Director</p>
      <p class="address">18 Orchard Lane, #04-12<br>Singapore 238841</p>
      <ul class="contact-list">
        <li>
          <svg viewBox="0 0 16 16" aria-hidden="true"><path d="M3.5 1.5l2.5 0 1 3.5-1.8 1.2a8 8 0 0 0 4.6 4.6L11 9l3.5 1v2.5c0 1-.8 2-2 2A11 11 0 0 1 1.5 3.5c0-1.2 1-2 2-2z"/></svg>
          <span>065-555 012 345</span>
        </li>
        <li>
          <svg viewBox="0 0 16 16" aria-hidden="true"><path d="M1 3h14v1.2L8 8.8 1 4.2z"/><path d="M1 5.6l7 4.6 7-4.6V13H1z"/></svg>
          <span>hello@brightpathbloom.sg</span>
        </li>
        <li>
          <svg viewBox="0 0 16 16" aria-hidden="true"><path d="M8 1a7 7 0 1 0 0 14A7 7 0 0 0 8 1zm0 1.6c.9 0 2 1.8 2.3 4.6H5.7C6 4.4 7.1 2.6 8 2.6zM2.7 8.8h1.9c.1 1.6.5 3 1 4a5.4 5.4 0 0 1-2.9-4zm0-1.6a5.4 5.4 0 0 1 2.9-4c-.5 1-.9 2.4-1 4zm5.3 6.2c-.9 0-2-1.8-2.3-4.6h4.6c-.3 2.8-1.4 4.6-2.3 4.6zm2.4-.6c.5-1 .9-2.4 1-4h1.9a5.4 5.4 0 0 1-2.9 4zm1-5.6c-.1-1.6-.5-3-1-4a5.4 5.4 0 0 1 2.9 4z"/></svg>
          <span>www.brightpathbloom.sg</span>
        </li>
      </ul>
    </div>
  </section>
</main>
</body>
</html>
```